Tallow Ridge Snacks is looking for a wrapper design for our flagship protein bar. A sleek and simple, yet powerful design is a must. A company that has a no BS attitude, no flashy artwork and straight to the point advertising is key. Focusing on Bodybuilders and Powerlifters, the wrapper does not need to appeal to the mass market. A dark, simple, and powerful vibe must be achieved. Less is more

Target Market(s)

Body Builders and Powerlifters

Industry/Entity Type

Supplement

Font styles to use
Decorative

Colors

Designer to choose colors to be used in the design.

Requirements
Must have
• Refer to "Legal Label Requirements" document.
• Refer to "Template Drawn" or "Wrapper.ai" for dimensions.
• *Must have the "Tallow Bar" logo stamped somewhere on the front of the bar**
• Sleek and powerful design
• Neutral /dark colors and possible accents with logo colors (use sparingly)
• Flavor of bar "Peanut Butter Crisp" must be displayed somewhere. Simple graphic can be included if goes well with overall design.
• Wrapper will be foil, so please make use of metallic effects by leaving sections/outlines transparent.
• Claims: (State it uses "Hydrolyzed Whey Protein" and contains 25g's of protein and only 6g's of sugar, as well as only real ingredients (These must be in French as well)
• Proudly Canadian stamp with flag somewhere.
• Social Media Icons (Instagram,Facebook) as well as website "tallowbarsnx.ca)
• Design must be able to work with future bar flavors, with only altering colors/flavor graphic (if necessary)
• *Will Include Nutritional Label and Ingredient List at a later date*
Nice to have
• I think a cool graphic of a simple hand and hammer outline using the metallic effect would be cool. Something that resembles the act of "forging metal" while demonstrating power, but isn't too distracting.
• A label mock up to see a general bar idea
Should not have
• Flashy/godly designs

```html
<!DOCTYPE html>
<html lang="en">
<head>
<meta charset="utf-8">
<title>Tallow Bar – Peanut Butter Crisp Wrapper</title>
<link rel="stylesheet" href="https://fonts.googleapis.com/css2?family=Pathway+Gothic+One&family=Saira+Semi+Condensed:wght@400&display=swap">
<style>
  :root {
    --page: #ffffff;
    --wrapper-dark: #1c1b1c;
    --wrapper-edge: #141314;
    --texture-light: #2a292a;
    --texture-dark: #191819;
    --accent-red: #e01f26;
    --accent-red-deep: #b8171d;
    --art-dark: #1a191a;
    --silver: #c9c9cb;
    --silver-soft: #b4b4b6;
  }
  * { margin: 0; padding: 0; box-sizing: border-box; }
  html, body {
    width: 1200px;
    height: 1000px;
    overflow: hidden;
    background: var(--page);
  }
  .canvas {
    position: relative;
    width: 1200px;
    height: 1000px;
  }
  .wrapper {
    position: absolute;
    left: 150px;
    top: 300px;
    width: 900px;
    height: 420px;
    background: var(--wrapper-dark);
    overflow: hidden;
  }
  .fold-band {
    position: absolute;
    left: 0;
    width: 100%;
    background: var(--wrapper-edge);
  }
  .fold-band--top { top: 0; height: 62px; }
  .fold-band--bottom { bottom: 0; height: 56px; }
  .texture-band {
    position: absolute;
    left: 0;
    top: 80px;
    width: 900px;
    height: 282px;
    background: linear-gradient(180deg, var(--texture-light) 0%, var(--texture-dark) 50%, var(--texture-light) 100%);
  }
  .accent-panel {
    position: absolute;
    inset: 0;
  }
  .artwork {
    position: absolute;
    left: 690px;
    top: 72px;
    width: 190px;
    height: 290px;
    background: linear-gradient(160deg, var(--art-dark) 0%, rgba(26,25,26,0.85) 60%, rgba(26,25,26,0.55) 100%);
    border-radius: 4px;
  }
  .brand-name {
    position: absolute;
    left: 66px;
    top: 122px;
    font-family: "Saira Semi Condensed", sans-serif;
    font-weight: 400;
    font-size: 34px;
    letter-spacing: 5px;
    color: var(--silver);
    line-height: 1;
    white-space: nowrap;
  }
  .flavor {
    position: absolute;
    left: 68px;
    top: 218px;
    font-family: "Pathway Gothic One", sans-serif;
    font-weight: 400;
    font-size: 38px;
    color: var(--silver);
    line-height: 1;
    white-space: nowrap;
  }
  .claims {
    position: absolute;
    left: 74px;
    top: 280px;
    list-style: none;
    font-family: "Pathway Gothic One", sans-serif;
    font-size: 13px;
    line-height: 20px;
    letter-spacing: 0.4px;
    color: var(--silver-soft);
  }
</style>
</head>
<body>
  <main class="canvas">
    <section class="wrapper" aria-label="Protein bar wrapper front">
      <div class="fold-band fold-band--top"></div>
      <div class="fold-band fold-band--bottom"></div>
      <div class="texture-band" role="img" aria-label="Dark faceted triangle texture across the wrapper body"></div>

      <svg class="accent-panel" viewBox="0 0 900 420" width="900" height="420" aria-hidden="true">
        <polygon points="675,0 900,0 900,420 490,420" fill="var(--accent-red)"/>
        <polygon points="860,0 900,0 900,420 820,420" fill="var(--accent-red-deep)" opacity="0.35"/>
      </svg>

      <div class="artwork" role="img" aria-label="Silhouette of a fist striking a hammer onto an anvil with spark lines"></div>

      <p class="brand-name">TALLOW BAR</p>
      <h1 class="flavor">Peanut Butter Crisp</h1>
      <ul class="claims">
        <li>Hydrolyzed Whey Protein</li>
        <li>25g's of protein</li>
        <li>6g's of sugar</li>
      </ul>
    </section>
  </main>
</body>
</html>
```